'Bright Ledger Hidden Keys' Book Cover

I need a professional book cover design for my new upcoming book that shows people how to get a high credit score.

Here are my two websites:

https://www.moneywordbank-lexa.info
https://moneywordbank-lexa.com/

I am looking for a clean, professional design that pops (emotional touch) and separates from the other books that are on the market. Cover aspect ratio 1:4 for Pagewisp version and 1:5 for the paperback version. Yellow or blue are good colors - but not must. See the basic examples that I provided. File delivery format PDF.

Book Title: Bright Ledger Hidden Keys
Byline: The Quick Lift And Mend Manual for Stellar Borrowing

Currently on Brindlecart pre-order:
https://www.brindlecart.example/Bright-Ledger-Hidden-Keys-Stellar-ebook/dp/Q48MPLRT71

I am the author of 36 published books on Brindlecart. My author profile is here:
brindlecart.example/author/gideonvarly

Targeted audience: People that want to improve or repair their bad credit score.

Target Market(s)

People/consumers in the US that want to improve or repair their credit score.

Industry/Entity Type

Consumer

Font styles to use
Sans Serif

Colors

Designer to choose colors to be used in the design.

Requirements
Must have
• Author name, Title, byline, and graphic element(s).
Nice to have
• - 2020 edition logo / batch

```html
<!DOCTYPE html>
<html lang="en">
<head>
<meta charset="utf-8">
<title>Bright Ledger Hidden Keys — Book Cover</title>
<link rel="stylesheet" href="https://fonts.googleapis.com/css2?family=Source+Sans+3:wght@700;900&family=Josefin+Sans:wght@400&display=swap">
<style>
  :root {
    --cover-yellow: #e8be00;
    --chart-yellow: #f4d000;
    --title-white: #ffffff;
    --subtitle-cream: #fdf6cf;
    --author-ink: #111111;
    --card-blue-light: #2a8fd6;
    --card-blue-dark: #0a5a9e;
    --trail-light: #fff6a8;
  }
  html, body {
    margin: 0;
    padding: 0;
    width: 794px;
    height: 1200px;
    overflow: hidden;
    background: var(--cover-yellow);
  }
  .cover {
    position: relative;
    width: 794px;
    height: 1200px;
    background: var(--cover-yellow);
    overflow: hidden;
  }
  .cover-art {
    position: absolute;
    inset: 0;
  }
  .title-main {
    font-family: "Source Sans 3", "Source Sans Pro", sans-serif;
    font-weight: 900;
    fill: var(--title-white);
  }
  .title-sub {
    font-family: "Source Sans 3", "Source Sans Pro", sans-serif;
    font-weight: 700;
    fill: var(--subtitle-cream);
  }
  .chart-line {
    fill: none;
    stroke: var(--chart-yellow);
    stroke-width: 5;
    stroke-linejoin: round;
  }
  .chart-dot {
    fill: var(--cover-yellow);
    stroke: var(--chart-yellow);
    stroke-width: 5;
  }
  .author-name {
    position: absolute;
    left: 0;
    right: 0;
    top: 1108px;
    margin: 0;
    text-align: center;
    font-family: "Josefin Sans", sans-serif;
    font-weight: 400;
    font-size: 35px;
    letter-spacing: 0.2em;
    color: var(--author-ink);
    padding-left: 0.2em;
  }
</style>
</head>
<body>
<main class="cover">
  <svg class="cover-art" width="794" height="1200" viewBox="0 0 794 1200" xmlns="http://www.w3.org/2000/svg">
    <defs>
      <linearGradient id="card-fill" x1="0" y1="0" x2="1" y2="1">
        <stop offset="0" stop-color="var(--card-blue-light)"/>
        <stop offset="1" stop-color="var(--card-blue-dark)"/>
      </linearGradient>
      <linearGradient id="trail-fill" x1="1" y1="0" x2="0" y2="1">
        <stop offset="0" stop-color="var(--trail-light)" stop-opacity="0.9"/>
        <stop offset="1" stop-color="var(--trail-light)" stop-opacity="0"/>
      </linearGradient>
    </defs>

    <!-- rising line chart, upper right -->
    <g class="chart chart-upper">
      <polyline class="chart-line" points="560,650 593,600 646,630 725,525"/>
      <circle class="chart-dot" cx="593" cy="600" r="10"/>
      <circle class="chart-dot" cx="646" cy="630" r="10"/>
      <circle class="chart-dot" cx="725" cy="525" r="12"/>
    </g>

    <!-- rising line chart, lower left -->
    <g class="chart chart-lower">
      <polyline class="chart-line" points="68,993 131,878 190,925 280,850"/>
      <circle class="chart-dot" cx="68" cy="993" r="12"/>
      <circle class="chart-dot" cx="131" cy="878" r="11"/>
      <circle class="chart-dot" cx="190" cy="925" r="11"/>
    </g>

    <!-- flying bank card illustration area -->
    <g role="img" aria-label="Illustration of a blue bank card with a gold chip flying up and to the right, trailing white and yellow speed streaks">
      <polygon points="330,760 420,700 260,1180 100,1180" fill="url(#trail-fill)"/>
      <rect x="-120" y="-150" width="240" height="330" rx="26"
            transform="translate(515,860) rotate(41)" fill="url(#card-fill)"/>
    </g>

    <!-- title block -->
    <text class="title-main" x="107" y="248" font-size="190" textLength="580" lengthAdjust="spacingAndGlyphs">BRIGHT</text>
    <text class="title-main" x="107" y="357" font-size="104" textLength="580" lengthAdjust="spacingAndGlyphs">LEDGER HIDDEN</text>
    <text class="title-main" x="107" y="473" font-size="114" textLength="580" lengthAdjust="spacing">KEYS</text>

    <text class="title-sub" x="108" y="542" font-size="41" textLength="578" lengthAdjust="spacing">The Quick Lift &amp; Mend Manual</text>
    <text class="title-sub" x="114" y="597" font-size="41" textLength="566" lengthAdjust="spacing">for Stellar Borrowing</text>
  </svg>

  <p class="author-name">GIDEON VARLY</p>
</main>
</body>
</html>
```